The (Private) News Sharing Report

This is a professional and academic report of 35 pages for journalists and teachers. The topic of the report is News Sharing: journalism, social networks and technology. Attached there is an example of the kind of design we are looking for: visual, fresh and modern.

Target Market(s)

Journalists, Journalism Students, Communication Researchers,

Industry/Entity Type

Media

Font styles to use
Sans Serif

Colors
3276b5
33a6d7
886aae
b868aa

Requirements
Must have
• Copyleft images, visual style
Nice to have
• There is an example attached.

```html
<!DOCTYPE html>
<html lang="en">
<head>
<meta charset="utf-8">
<title>The (Private) News Sharing Report — page spreads</title>
<link href="https://fonts.googleapis.com/css2?family=Source+Sans+3:ital,wght@0,400;0,600;0,700;1,400&display=swap" rel="stylesheet">
<style>
  :root{
    --navy:#3276b5;
    --sky:#33a6d7;
    --purple:#886aae;
    --magenta:#b868aa;
    --ink:#1f1f1f;
    --paper:#ffffff;
    --board:#b4b3b2;
  }
  *{box-sizing:border-box;margin:0;padding:0}
  html,body{width:1200px;height:1200px;overflow:hidden;background:var(--board)}
  body{position:relative;font-family:"Source Sans 3",sans-serif;color:var(--ink)}
  .page{position:absolute;background:var(--paper);overflow:hidden;box-shadow:0 2px 6px rgba(0,0,0,.18)}
  .page svg.deco{position:absolute;left:0;top:0;width:100%;height:100%}
  .abs{position:absolute}

  /* cover */
  .cover{left:91px;top:37px;width:463px;height:597px}
  .cover-title{left:158px;top:292px;width:300px}
  .cover-title h1{font-size:17px;font-weight:700;line-height:1.2}
  .cover-title p{font-size:16px;line-height:1.2;font-weight:400}
  .cover-credit{left:158px;top:478px;width:290px;font-size:9.4px;line-height:12px}
  .cover-credit strong{font-weight:700}
  .cover-year{left:27px;top:555px;font-size:16px}
  .cover-year::before{content:"";position:absolute;left:0;top:-4px;width:34px;height:3px;background:var(--sky)}

  /* credits */
  .credits{left:614px;top:37px;width:463px;height:597px}
  .credits-text{left:200px;top:108px;width:237px;font-size:9.2px;line-height:13.6px;text-align:justify}
  .credits-text p+p{margin-top:13.6px}
  .credits-text b{font-weight:700}

  /* index */
  .index{left:30px;top:683px;width:352px;height:455px}
  .index-label{left:82px;top:22px;transform-origin:left top;transform:rotate(-90deg) translateX(-52px);font-size:12px;letter-spacing:4px;color:var(--purple);font-weight:600}
  .index-band{left:21px;top:82px;right:0;height:14px;background:var(--magenta)}
  .toc{left:84px;top:112px;width:200px;list-style:none;font-size:8.4px}
  .toc li{position:absolute;left:0;width:188px;display:flex;justify-content:space-between;align-items:center}
  .toc .main{font-weight:600}
  .toc .sub{left:6px;width:182px;font-style:italic}
  .toc .num{display:inline-flex;align-items:center;justify-content:center;width:16px;height:16px;border-radius:50%;background:var(--purple);color:#fff;font-style:normal;font-size:9px;margin-right:5px}

  /* intro */
  .intro{left:410px;top:683px;width:354px;height:458px}
  .page-heading{font-size:19px;font-weight:700;color:var(--purple);line-height:1}
  .intro .page-heading{left:21px;top:52px}
  .intro-cols{left:85px;top:80px;width:249px;column-count:2;column-gap:7px;column-fill:auto;font-size:6.7px;line-height:9.3px;text-align:justify;height:340px}
  .intro-cols p+p{margin-top:9px}
  .folio{position:absolute;background:var(--purple);color:#fff;font-size:6px;font-weight:700;display:flex;align-items:center;justify-content:center}

  /* questions */
  .questions{left:790px;top:681px;width:358px;height:463px}
  .questions .page-heading{left:21px;top:80px}
  .questions-lead{left:22px;top:104px;font-size:8px;font-weight:600;line-height:9px;width:160px}
  .rq{position:absolute;font-size:7px;line-height:8.5px}
  .rq-tag{display:block;width:13px;height:10px;background:var(--magenta);color:#fff;font-size:7px;font-weight:700;text-align:center;line-height:10px}
  .rq-text{display:block;border-top:1px solid var(--sky);padding-top:3px}
</style>
</head>
<body>

<!-- cover -->
<section class="page cover">
  <svg class="deco" viewBox="0 0 463 597" aria-hidden="true">
    <polygon points="0,0 463,0 0,345" fill="var(--purple)"/>
    <line x1="463" y1="11" x2="130" y2="265" stroke="var(--sky)" stroke-width="1.6"/>
    <line x1="435" y1="51" x2="0" y2="378" stroke="var(--magenta)" stroke-width="1.6"/>
    <circle cx="182" cy="414" r="21" fill="none" stroke="var(--ink)" stroke-width="4"/>
    <rect x="158" y="551" width="305" height="18" fill="var(--magenta)"/>
  </svg>
  <div class="abs cover-title">
    <h1>The (Private) News Sharing Report</h1>
    <p>A starting guide for researchers<br>and journalists</p>
  </div>
  <div class="abs cover-credit">
    <strong>A report by Martín Aldana-Serra</strong><br>
    Visiting Scholar at Capitol Hill University (Washington, D.C., USA) with the help of Research Grants 18/19 from the Meridian University of Levante (Murcia, Spain)
  </div>
  <div class="abs cover-year">2019</div>
</section>

<!-- credits -->
<section class="page credits">
  <svg class="deco" viewBox="0 0 463 597" aria-hidden="true">
    <rect x="0" y="0" width="185" height="597" fill="var(--purple)"/>
    <line x1="27" y1="103" x2="436" y2="103" stroke="var(--sky)" stroke-width="1.4"/>
    <line x1="27" y1="103" x2="185" y2="103" stroke="var(--navy)" stroke-width="1.4"/>
    <line x1="326" y1="0" x2="50" y2="184" stroke="var(--magenta)" stroke-width="1.4"/>
  </svg>
  <div class="abs credits-text">
    <p>This is a report by Martín Aldana Serra (PhD), a journalist working at the Meridian University of Levante (MUL, Spain), where he is the Head of the Communication Sciences Department. This project has been supported by a research grant from MUL to do a research stay as a Visiting Scholar at Capitol Hill University (CHU), USA, and the help of professor Helen Marsh at CHU.</p>
    <p>Special thanks goes to those who collaborated in the interviews: the journalists at the Global Newsroom Institute (GNI), The Harbor Ledger, Northlight Media Network, Canal Sol, The Civic Accountability Desk, The Iberia Brief, Verifica and Contraste. In addition, I also want to thank the whole faculty at the School of Communication at Capitol Hill University (CHU-SOC), who always offered their collaboration.</p>
    <p>Special thanks also goes to colleagues and scholars who selflessly dedicated their time to talk and hold meetings. They shed light on many topics reflected in the report. They are Tomás Lindqvist, Rafi Okonjo, Elena Brandt-Ruiz, Paula Werner, Nina Castell, Quique Robles, Gerald Hastings, and Marion Pike.</p>
    <p>The interviews are expressions of personal opinions as journalists and they do not necessarily express the official point of view of the media where they work. Inquiries for further information about this research can be sent to <b>m.aldana@mailbox.example</b> or <b>m.aldana@mul.example</b></p>
  </div>
</section>

<!-- index -->
<section class="page index">
  <svg class="deco" viewBox="0 0 352 455" aria-hidden="true">
    <polygon points="0,443 352,414 352,455 0,455" fill="var(--purple)"/>
    <line x1="0" y1="429" x2="223" y2="407" stroke="var(--magenta)" stroke-width="1.4"/>
    <line x1="114" y1="426" x2="352" y2="404" stroke="var(--sky)" stroke-width="1.4"/>
  </svg>
  <div class="abs index-label">INDEX</div>
  <div class="abs index-band"></div>
  <ul class="abs toc">
    <li style="top:0">Introduction<span>4</span></li>
    <li class="main" style="top:23px">Research Questions<span>5</span></li>
    <li class="sub" style="top:44px"><span><span class="num">1.</span>The Media Landscape</span><span>6</span></li>
    <li class="sub" style="top:66px"><span><span class="num">2.</span>The Interviews</span><span>11</span></li>
    <li class="sub" style="top:89px"><span><span class="num">3.</span>The Best Practices</span><span>29</span></li>
    <li class="sub" style="top:112px"><span><span class="num">4.</span>Conclusions</span><span>31</span></li>
    <li style="top:135px">References<span>33</span></li>
  </ul>
</section>

<!-- introduction -->
<section class="page intro">
  <svg class="deco" viewBox="0 0 354 458" aria-hidden="true">
    <line x1="21" y1="73" x2="333" y2="73" stroke="var(--sky)" stroke-width="1.2"/>
    <rect x="213" y="416" width="121" height="5" fill="var(--magenta)"/>
  </svg>
  <h2 class="abs page-heading">Introduction</h2>
  <div class="abs intro-cols">
    <p>The job of journalists is not just longer on the internet because it ends later, it is also longer because it starts before. On the web, on the one hand, a journalist can have a community even before having a journalistic product. On the other hand, social recommendations, incidental consumption of news and online private messages are giving a broader reach to journalism, as we know it now.</p>
    <p>Because publishing is not the end of the journalistic routine, the whole process now is longer. You cannot fully understand what “news” means for people if you do not understand how and why they are sharing the news on online private platforms. Private messaging networks are adding new challenges to journalists and the media. When we are talking about online private environments, issues such as sources, fact-checking, misinformation, privacy or (fake) news are being redefined, as well as the notions of trust, community, public service and media literacy.</p>
    <p>In 2018 a presidential candidate was accused of running a whole fake news campaign through ChatLine with hundreds of millions of messages against his opponent. This scandal is just an example of the growing relevance of fact-checking and the need to for media literacy skills among users of private messaging networks.</p>
    <p>Many news sites added a ChatLine sharing option in their news during the last few years (Harlow, 2014) and it seems like private channels, such as this one, could become a “major traffic driver for news sites” (Vance, R., Ost, L., &amp; Pell, J., 2015: 10). We cannot entirely know what people are doing with news in private messaging networks, but what we can see is what the media and journalists are doing with these platforms. This report is a draft of these actions.</p>
    <p>In news sharing research, a new broad theoretical foundation is needed, with quantitative studies, digital ethnographies or uses and gratifications approaches, and even combining these proaches and deriving new ones. We utilize the results of this preliminary research to provide insights so that journalism can be improved, and academic research of journalism can move forward in news sharing research.</p>
    <p>The main goal of this executive report is to help journalists and researchers get a deeper understanding of the news sharing processes in private networks. Share it, but not in a private way. Make it as public as you can.</p>
  </div>
  <div class="folio" style="left:22px;top:421px;width:14px;height:37px">4</div>
</section>

<!-- research questions -->
<section class="page questions">
  <svg class="deco" viewBox="0 0 358 463" aria-hidden="true">
    <line x1="21" y1="74" x2="337" y2="74" stroke="var(--sky)" stroke-width="1.2"/>
    <line x1="155" y1="0" x2="291" y2="119" stroke="var(--magenta)" stroke-width="1.2"/>
    <line x1="25" y1="346" x2="159" y2="463" stroke="var(--magenta)" stroke-width="1.2"/>
    <line x1="14" y1="463" x2="102" y2="365" stroke="var(--sky)" stroke-width="1.2"/>
    <circle cx="229" cy="126" r="17" fill="none" stroke="var(--ink)" stroke-width="3.5"/>
  </svg>
  <h2 class="abs page-heading">Research Questions</h2>
  <p class="abs questions-lead">This report is divided into the following six research questions:</p>

  <div class="rq" style="left:86px;top:153px;width:122px"><span class="rq-tag">1</span><span class="rq-text">How appropriate are private online messaging networks for journalism?</span></div>
  <div class="rq" style="left:121px;top:194px;width:210px"><span class="rq-tag">2</span><span class="rq-text">Can private messaging be useful for building trust between the media/journalists and communities?</span></div>
  <div class="rq" style="left:86px;top:236px;width:170px"><span class="rq-tag">3</span><span class="rq-text">How can journalists use private channels/platforms to be part of a community?</span></div>
  <div class="rq" style="left:121px;top:277px;width:170px"><span class="rq-tag">4</span><span class="rq-text">What are the new skills that the media landscape is requiring of journalists?</span></div>
  <div class="rq" style="left:86px;top:318px;width:170px"><span class="rq-tag">5</span><span class="rq-text">What are the new skills that the media landscape is requiring of journalists?</span></div>
  <div class="rq" style="left:121px;top:358px;width:218px"><span class="rq-tag">6</span><span class="rq-text">What are the best media practices with private online messaging?</span></div>

  <div class="folio" style="left:321px;top:424px;width:16px;height:39px">5</div>
</section>

</body>
</html>
```